Velmora Business Card

We need a design for business cards for our new company. We are a resident safety and security company company that focuses on senior living communities. we provide Nurse call, Access control, CCTV, Wired and wireless network infrastructure, Wander Management, and much more!

Our logo is the circuit board shield. Representing our high tech security solutions. I would like the business card to bring the same theme with perhaps some circuit board traces around the card similar to our logo

```html
<!DOCTYPE html>
<html lang="en">
<head>
<meta charset="utf-8">
<title>Velmora Business Card</title>
<link href="https://fonts.googleapis.com/css2?family=Montserrat:wght@400;500;600;800&display=swap" rel="stylesheet">
<style>
  :root {
    --stage: #1c1c1e;
    --paper: #ffffff;
    --brand-blue: #0a5ad4;
    --sky-blue: #00b6f5;
    --ink: #1a1a1a;
    --back-dark: #161617;
    --back-mid: #2c2c2e;
    --back-light: #4a4a4c;
  }
  * { margin: 0; padding: 0; box-sizing: border-box; }
  html, body {
    width: 1200px; height: 900px; overflow: hidden;
    background: var(--stage);
    font-family: "Montserrat", sans-serif;
  }
  .card {
    position: absolute; left: 320px;
    width: 560px; height: 320px;
    border-radius: 20px;
    overflow: hidden;
  }
  .card-front { top: 90px; background: var(--paper); }
  .card-back { top: 470px; background: var(--back-dark); }

  /* front */
  .brand {
    position: absolute; left: 35px; top: 118px; width: 200px;
    display: flex; align-items: center; justify-content: center; gap: 10px;
  }
  .brand-dot {
    width: 26px; height: 26px; border-radius: 50%;
    background: var(--brand-blue); flex: none;
  }
  .brand-name {
    color: var(--brand-blue); font-weight: 600; font-size: 30px;
    letter-spacing: 1px;
  }
  .divider {
    position: absolute; left: 247px; top: 80px;
    width: 2px; height: 155px; background: var(--brand-blue);
  }
  .contact { position: absolute; left: 267px; top: 82px; color: var(--ink); }
  .person-name {
    color: var(--brand-blue); font-weight: 800; font-size: 24px;
    letter-spacing: 1.5px; text-transform: uppercase; line-height: 1;
  }
  .person-title { font-size: 12.5px; margin-top: 4px; }
  .address { font-size: 12.5px; line-height: 1.3; margin-top: 14px; }
  .lines { list-style: none; margin-top: 9px; font-size: 12.5px; line-height: 1.4; }
  .lines li { display: flex; align-items: center; gap: 6px; }
  .lines svg { width: 12px; height: 12px; flex: none; }
  .band {
    position: absolute; left: 0; top: 252px; width: 440px; height: 27px;
    background: var(--brand-blue);
    clip-path: polygon(0 0, 100% 0, 96% 100%, 0 100%);
  }
  .band-accent {
    position: absolute; left: 400px; top: 279px; width: 160px; height: 24px;
    background: var(--sky-blue);
  }
  .website {
    position: absolute; left: 95px; top: 257px;
    color: var(--paper); font-weight: 600; font-size: 14px; letter-spacing: 1.5px;
  }
  .band-mark {
    position: absolute; left: 413px; top: 264px;
    width: 27px; height: 27px; border-radius: 50%;
    background: var(--paper); border: 2px solid var(--brand-blue);
  }

  /* back */
  .back-pattern {
    position: absolute; inset: 0;
    background:
      radial-gradient(ellipse at 85% 15%, var(--back-light) 0%, transparent 45%),
      radial-gradient(ellipse at 15% 90%, var(--back-mid) 0%, transparent 55%),
      linear-gradient(135deg, var(--back-mid) 0%, var(--back-dark) 60%);
  }
  .back-brand {
    position: absolute; right: 60px; top: 135px;
    display: flex; align-items: center; gap: 12px;
  }
  .back-brand .brand-dot { width: 34px; height: 34px; }
  .back-brand .brand-name { font-size: 32px; }
</style>
</head>
<body>
  <div class="card card-front">
    <div class="brand">
      <span class="brand-dot"></span>
      <span class="brand-name">Velmora</span>
    </div>
    <div class="divider"></div>
    <div class="contact">
      <div class="person-name">Martin Hale</div>
      <div class="person-title">President</div>
      <div class="address">418 Linden Road,<br>Suite #204</div>
      <ul class="lines">
        <li>
          <svg viewBox="0 0 24 24"><path fill="#0a5ad4" d="M6.6 10.8a15.1 15.1 0 0 0 6.6 6.6l2.2-2.2a1 1 0 0 1 1-.25 11.4 11.4 0 0 0 3.6.57 1 1 0 0 1 1 1V20a1 1 0 0 1-1 1A17 17 0 0 1 3 4a1 1 0 0 1 1-1h3.5a1 1 0 0 1 1 1c0 1.25.2 2.45.57 3.57a1 1 0 0 1-.25 1z"/></svg>
          (555) 014-2290
        </li>
        <li>
          <svg viewBox="0 0 24 24"><path fill="#0a5ad4" d="M3 8c0-2 4-4 9-4s9 2 9 4v2h-5V8H8v2H3zM6 12h12l2 8H4zm6 2.5a2.5 2.5 0 1 0 0 5 2.5 2.5 0 0 0 0-5z"/></svg>
          (555) 014-7731
        </li>
        <li>
          <svg viewBox="0 0 24 24"><rect x="3" y="6" width="18" height="12" fill="none" stroke="#0a5ad4" stroke-width="2"/><path d="M3 6l9 7 9-7" fill="none" stroke="#0a5ad4" stroke-width="2"/></svg>
          martin@velmora.com
        </li>
      </ul>
    </div>
    <div class="band-accent"></div>
    <div class="band"></div>
    <div class="website">www.velmora.com</div>
    <div class="band-mark"></div>
  </div>

  <div class="card card-back">
    <div class="back-pattern" role="img" aria-label="Embossed repeating circuit-board shield pattern in glossy black"></div>
    <div class="back-brand">
      <span class="brand-dot"></span>
      <span class="brand-name">Velmora</span>
    </div>
  </div>
</body>
</html>
```